Austrian finance und insurance broker needs business card design

We Need a serious looking Design for Business Card. we consult private and corporates customers in finance and insurance questions. the final design should express security and experience. We consult customers in questions of loans, Investments and insurance and have a wide range of Banks to offer. We compare several offers and select the best for our customers.

Target Market(s)

private and coporate customers with efforts in Money and insurance

Industry/Entity Type

Insurance Broker

Contact Information for Business Card

Bernhard Aigner
Geschäftsführer
staatl. geprüfter Vermögensberater und Versicherungsmakler
Tel: 0664 521 8409
office@der-brandl.at
www.der-brandl.at
Leopold Hainz Gasse 14
2183 Melkstetten
GISA Nr. 48270315 u. 51736048 (backside)

Font styles to use
Serif
Sans Serif

Requirements
Must have
• logo (designcrowd zip) and all Details
Nice to have
• makler logo design, maybe a 2 coloured Version is possible

```html
<!DOCTYPE html>
<html lang="de">
<head>
<meta charset="utf-8">
<title>Aigner Vermögensberatung – Visitenkarte</title>
<link rel="stylesheet" href="https://fonts.googleapis.com/css2?family=Lato:wght@400;700;900&display=swap">
<style>
  :root {
    --charcoal: #2e2d33;
    --brand-blue: #2a58b4;
    --paper: #ffffff;
    --tab-grey: #c8c8cc;
    --badge-red: #c8102e;
    --ink: #2b2b2b;
    --backdrop: #e8e6e2;
  }
  * { margin: 0; padding: 0; box-sizing: border-box; }
  html, body {
    width: 1200px; height: 942px; overflow: hidden;
    background: var(--backdrop);
    font-family: "Lato", Arial, sans-serif;
  }
  .card {
    position: absolute; left: 250px;
    width: 700px; height: 412px;
    overflow: hidden;
    box-shadow: 0 8px 24px rgba(0,0,0,0.25);
  }
  .card--front { top: 39px; background: var(--paper); }
  .card--back  { top: 491px; background: var(--charcoal); }
  .card__shapes { position: absolute; inset: 0; }
  .text { position: absolute; white-space: nowrap; }

  /* front */
  .brand-mark { position: absolute; left: 30px; top: 34px; }
  .brand-name { left: 104px; top: 48px; font-size: 17px; font-weight: 700; color: var(--brand-blue); }
  .brand-tagline { left: 104px; top: 72px; font-size: 13px; color: var(--ink); }
  .partner-badge { position: absolute; left: 40px; top: 118px; }

  .holder { left: 492px; top: 160px; color: #fff; }
  .holder__name { font-size: 26px; font-weight: 900; }
  .holder__role { font-size: 16px; font-weight: 700; margin-top: 4px; }
  .holder__qual { font-size: 13px; line-height: 1.35; margin-top: 6px; }

  .address { left: 30px; top: 248px; color: #fff; font-size: 18px; display: flex; align-items: center; gap: 12px; }
  .contact-row { left: 30px; top: 340px; right: 30px; display: flex; justify-content: space-between; color: #fff; font-size: 18px; }
  .contact-item { display: flex; align-items: center; gap: 10px; }

  /* back */
  .back-mark { position: absolute; left: 70px; top: 66px; }
  .back-name { left: 192px; top: 88px; font-size: 25px; font-weight: 700; color: var(--brand-blue); }
  .back-tagline { left: 192px; top: 126px; font-size: 19px; color: #fff; }
  .registry { left: 34px; top: 262px; font-size: 20px; color: #fff; }
</style>
</head>
<body>

<section class="card card--front" aria-label="Visitenkarte Vorderseite">
  <svg class="card__shapes" viewBox="0 0 700 412" width="700" height="412" aria-hidden="true">
    <rect class="tab" x="452" y="120" width="90" height="70" rx="14" fill="var(--tab-grey)"/>
    <rect class="address-band" x="0" y="222" width="500" height="76" fill="var(--brand-blue)"/>
    <path class="name-panel" d="M487 140 H700 V298 H472 V155 Q472 140 487 140 Z" fill="var(--brand-blue)"/>
    <path class="contact-band" d="M0 298 H560 C600 298 612 262 650 262 H700 V412 H0 Z" fill="var(--charcoal)"/>
  </svg>

  <svg class="brand-mark" width="62" height="62" viewBox="0 0 62 62" aria-hidden="true">
    <circle cx="31" cy="31" r="27" fill="none" stroke="var(--brand-blue)" stroke-width="4"/>
  </svg>
  <div class="text brand-name">Aigner Vermögensberatung GmbH</div>
  <div class="text brand-tagline">Finanzieren, Versichern, Vorsorgen</div>

  <svg class="partner-badge" width="44" height="44" viewBox="0 0 44 44" role="img" aria-label="Partnersiegel">
    <circle cx="22" cy="22" r="21" fill="var(--badge-red)"/>
  </svg>

  <div class="text holder">
    <div class="holder__name">Bernhard Aigner</div>
    <div class="holder__role">Geschäftsführer</div>
    <div class="holder__qual">staatl. geprüfter Vermögensberater<br>und Versicherungsmakler</div>
  </div>

  <div class="text address">
    <svg width="16" height="22" viewBox="0 0 16 22" aria-hidden="true">
      <path d="M8 0 C3.6 0 0 3.4 0 7.8 C0 13 8 22 8 22 C8 22 16 13 16 7.8 C16 3.4 12.4 0 8 0 Z" fill="#fff"/>
      <circle cx="8" cy="8" r="3" fill="var(--brand-blue)"/>
    </svg>
    <span>Leopold Hainz Gasse 14, 2183 Melkstetten</span>
  </div>

  <div class="text contact-row">
    <div class="contact-item">
      <svg width="18" height="18" viewBox="0 0 24 24" aria-hidden="true">
        <path d="M6.6 10.8a15.1 15.1 0 0 0 6.6 6.6l2.2-2.2a1 1 0 0 1 1-.25 11.4 11.4 0 0 0 3.6.57 1 1 0 0 1 1 1V20a1 1 0 0 1-1 1A17 17 0 0 1 3 4a1 1 0 0 1 1-1h3.5a1 1 0 0 1 1 1c0 1.25.2 2.450.57 3.6a1 1 0 0 1-.25 1z" fill="var(--brand-blue)"/>
      </svg>
      <span>0664 521 8409</span>
    </div>
    <div class="contact-item">
      <svg width="18" height="18" viewBox="0 0 18 18" aria-hidden="true">
        <rect x="0" y="2" width="18" height="14" fill="var(--brand-blue)"/>
        <path d="M3 8 L7.5 12 L15 4" fill="none" stroke="var(--charcoal)" stroke-width="2"/>
      </svg>
      <span>office@der-brandl.at</span>
    </div>
    <div class="contact-item">
      <svg width="18" height="18" viewBox="0 0 20 20" aria-hidden="true">
        <g fill="none" stroke="var(--brand-blue)" stroke-width="1.6">
          <circle cx="10" cy="10" r="8.5"/>
          <ellipse cx="10" cy="10" rx="4" ry="8.5"/>
          <path d="M1.5 10 H18.5 M3 5.5 H17 M3 14.5 H17"/>
        </g>
      </svg>
      <span>www.der-brandl.at</span>
    </div>
  </div>
</section>

<section class="card card--back" aria-label="Visitenkarte Rückseite">
  <svg class="card__shapes" viewBox="0 0 700 412" width="700" height="412" aria-hidden="true">
    <path class="registry-band" d="M0 228 H360 L312 318 H0 Z" fill="var(--brand-blue)"/>
  </svg>
  <svg class="back-mark" width="104" height="104" viewBox="0 0 104 104" aria-hidden="true">
    <circle cx="52" cy="52" r="46" fill="none" stroke="var(--brand-blue)" stroke-width="5"/>
  </svg>
  <div class="text back-name">Aigner Vermögensberatung GmbH</div>
  <div class="text back-tagline">Finanzieren, Versichern, Vorsorgen</div>
  <div class="text registry">GISA Nr. 48270315 u. 51736048</div>
</section>

</body>
</html>
```